Business Card for Consulting Company

I would need a business card for my consulting company - the company brand and logos are defined and shared as part of this project. The proposed design for the business card can be reused as inspiration for my email signature.

```html
<!DOCTYPE html>
<html lang="en">
<head>
<meta charset="UTF-8">
<title>Talentora — Business Card</title>
<link rel="stylesheet" href="https://fonts.googleapis.com/css2?family=Exo+2:wght@400;500;600&display=swap">
<style>
  :root {
    --teal: #05a9ad;
    --teal-deep: #048f93;
    --ink: #3a3a3c;
    --ink-soft: #4a4a4d;
    --rule: #cfd3d4;
    --paper: #ffffff;
    --backdrop: #c9c9c9;
  }
  * { box-sizing: border-box; margin: 0; padding: 0; }
  html, body {
    width: 1200px;
    height: 900px;
    overflow: hidden;
  }
  body {
    background: var(--backdrop);
    font-family: "Exo 2", sans-serif;
    position: relative;
  }
  .card {
    position: absolute;
    width: 560px;
    height: 320px;
    border-radius: 26px;
    box-shadow: 0 6px 14px rgba(0,0,0,0.25);
    overflow: hidden;
  }

  /* Reverse side */
  .card--back {
    left: 80px;
    top: 110px;
    background: var(--teal);
  }
  .card--back .back-mark {
    position: absolute;
    right: 56px;
    top: 50%;
    transform: translateY(-50%);
    display: flex;
    align-items: center;
    gap: 16px;
    color: var(--paper);
    font-weight: 500;
    font-size: 34px;
    letter-spacing: 1px;
  }
  .back-mark .dot {
    width: 40px;
    height: 40px;
    border-radius: 50%;
    background: var(--teal-deep);
  }

  /* Front side */
  .card--front {
    left: 560px;
    top: 470px;
    background: var(--paper);
  }
  .contact {
    position: absolute;
    left: 44px;
    top: 92px;
  }
  .contact .name {
    font-size: 30px;
    font-weight: 600;
    color: var(--ink);
    letter-spacing: 0.5px;
    line-height: 1;
  }
  .contact .name .surname { color: var(--teal); }
  .contact .role {
    margin-top: 6px;
    font-size: 15px;
    color: var(--ink-soft);
    letter-spacing: 1px;
  }
  .details {
    list-style: none;
    margin-top: 22px;
  }
  .details li {
    display: flex;
    align-items: center;
    gap: 10px;
    font-size: 14px;
    color: var(--ink);
    letter-spacing: 0.5px;
    line-height: 24px;
  }
  .details svg { width: 16px; height: 16px; flex: none; }
  .details .accent { color: var(--teal); }

  .divider {
    position: absolute;
    left: 340px;
    top: 70px;
    width: 1px;
    height: 180px;
    background: var(--rule);
  }
  .brand {
    position: absolute;
    left: 341px;
    right: 0;
    top: 0;
    bottom: 0;
    display: flex;
    align-items: center;
    justify-content: center;
    gap: 10px;
  }
  .brand .dot {
    width: 18px;
    height: 18px;
    border-radius: 50%;
    background: var(--ink);
  }
  .brand .brand-name {
    font-size: 32px;
    font-weight: 500;
    color: var(--teal);
    letter-spacing: 0.5px;
  }
</style>
</head>
<body>

  <section class="card card--back" aria-label="Card reverse">
    <div class="back-mark">
      <span class="dot"></span>
      <span class="brand-name">Talentora</span>
    </div>
  </section>

  <section class="card card--front" aria-label="Card front">
    <div class="contact">
      <h1 class="name">Marcel <span class="surname">Verhoef</span></h1>
      <p class="role">Founder &amp; CEO</p>
      <ul class="details">
        <li>
          <svg viewBox="0 0 16 16" aria-hidden="true"><path d="M4 1.5 6 4 4.8 5.6c.8 1.9 2.3 3.4 4.2 4.2L10.6 8.6 13 10.6 11.6 13C7 12.6 3.4 9 3 4.4Z" fill="var(--teal)"/></svg>
          <span>044-555 210 318</span>
        </li>
        <li>
          <svg viewBox="0 0 16 16" aria-hidden="true"><rect x="1" y="3.5" width="14" height="9" rx="1" fill="var(--teal)"/><path d="M1.5 4 8 9l6.5-5" fill="none" stroke="#fff" stroke-width="1.2"/></svg>
          <span>marcel.verhoef@talentora.eu</span>
        </li>
        <li>
          <svg viewBox="0 0 16 16" aria-hidden="true"><g fill="none" stroke="var(--teal)" stroke-width="1.3"><circle cx="8" cy="8" r="6.5"/><ellipse cx="8" cy="8" rx="2.8" ry="6.5"/><path d="M1.5 8h13M2.5 4.7h11M2.5 11.3h11"/></g></svg>
          <span>www.<span class="accent">talentora</span>.eu</span>
        </li>
      </ul>
    </div>

    <div class="divider"></div>

    <div class="brand">
      <span class="dot"></span>
      <span class="brand-name">Talentora</span>
    </div>
  </section>

</body>
</html>
```